Business needs stationary

We are a company how capital venture and investment webcompany and work for international clients.

We need a stationary for a;

- email template
- business card
- web logo

Use the colors and elements plus company name in the attachment

Business card must include:

- company
- title
- adress
- phonenumber
- email adress
- website adress
- twitter
- facebook

We use the janeausten font. it's free. http://www.glyphtrove.example/mirel-quay.font

```html
<!DOCTYPE html>
<html lang="en">
<head>
<meta charset="utf-8">
<title>Corwen Halstead – Newsletter</title>
<link rel="stylesheet" href="https://fonts.googleapis.com/css2?family=Quicksand:wght@400;500;600&display=swap">
<style>
  :root {
    --navy: #0d4a63;
    --accent: #f26b3a;
    --sand: #eadfd0;
    --ink: #1f1f1f;
    --muted: #9a9a9a;
    --link: #555555;
    --white: #ffffff;
  }
  * { box-sizing: border-box; margin: 0; padding: 0; }
  html, body {
    width: 1136px;
    height: 1200px;
    overflow: hidden;
    background: var(--white);
    font-family: "Quicksand", sans-serif;
    color: var(--ink);
  }
  .newsletter {
    position: relative;
    width: 884px;
    margin-left: 126px;
  }
  .masthead {
    height: 288px;
    background: var(--navy);
    display: flex;
    flex-direction: column;
    align-items: center;
    padding-top: 70px;
    color: var(--white);
  }
  .masthead__mark {
    width: 64px;
    height: 60px;
    background: var(--accent);
  }
  .masthead__name {
    margin-top: 22px;
    font-size: 52px;
    font-weight: 500;
    line-height: 1;
  }
  .masthead__tagline {
    margin-top: 14px;
    font-size: 19px;
    font-weight: 500;
    line-height: 22px;
    text-align: center;
    text-transform: uppercase;
    letter-spacing: 0.5px;
  }
  .rule {
    height: 3px;
    background: var(--navy);
  }
  .rule--top { margin-top: 19px; }
  .article { padding: 48px 0 52px; }
  .article__title {
    font-size: 40px;
    font-weight: 400;
    line-height: 1.2;
    margin-bottom: 28px;
  }
  .article__body {
    font-size: 20px;
    line-height: 28px;
    text-align: justify;
    font-weight: 500;
  }
  .footer {
    position: relative;
    padding: 25px 0 0 6px;
  }
  .footer__brand {
    display: flex;
    align-items: center;
    gap: 14px;
  }
  .footer__mark {
    width: 40px;
    height: 39px;
    background: var(--accent);
  }
  .footer__name {
    font-size: 32px;
    font-weight: 500;
    color: var(--ink);
  }
  .footer__tagline {
    margin: 13px 0 0 12px;
    font-size: 15px;
    font-weight: 500;
    font-style: italic;
  }
  .footer__contact {
    margin: 26px 0 0 12px;
    font-size: 18px;
    line-height: 26px;
    color: var(--muted);
    font-weight: 500;
  }
  .footer__prefs {
    margin-top: 76px;
    font-size: 18px;
    line-height: 25px;
    color: var(--link);
    font-weight: 500;
  }
  .footer__prefs a { color: var(--link); text-decoration: underline; }
  .social {
    position: absolute;
    top: 25px;
    right: 34px;
    display: flex;
    gap: 9px;
  }
  .social__item {
    width: 45px;
    height: 43px;
    border-radius: 4px;
    background: var(--accent);
  }
</style>
</head>
<body>
  <main class="newsletter">
    <header class="masthead">
      <div class="masthead__mark"></div>
      <div class="masthead__name">Corwen Halstead</div>
      <div class="masthead__tagline">Capital Venture &amp;<br>Investment Web Company</div>
    </header>
    <div class="rule rule--top"></div>

    <article class="article">
      <h1 class="article__title">Lorem ipsum dolor sit amet</h1>
      <p class="article__body">Consectetur adipiscing elit. Phasellus a ipsum a risus volutpat placerat in nec mauris. Fusce sit amet enim erat, in sagittis arcu. Aliquam dolor dolor, semper id tempor et, varius pulvinar tellus. Maurtis commodo urna at dui bibendum quis euismod velit egestas. Vestibulum ante ipsum primis in faucibus orci luctus et. ultrices posuere cubilia Curae; Proin adipiscing, arcu id imperdiet vulputate, est elit ultrices augue, vitae bibendum ipsum elit vitae quam. Donec augue ipsum, gravida quis pellentesque nec, tempor at velit. Donec ultricies eleifend turpis, sed gravida turpis volutpat in. Pellentesque orci dolor, suscipit vel adipiscing quis, vehicula vel lacus. In a dui elit, sit amet tincidunt eros. Sed velit lorem, molestie sed scelerisque vitae, volutpat sit amet ante. Aliquam id felis in justo feugiat ultrices. Aliquam id eros magna, ac gravida odio. Sed sed auctor ante. Ut risus enim, venenatis non hendrerit eu, hendrerit non eros. Fusce nec purus turpis. Nunc rutrum, arcu nec porta gravida, orci lectus ullamcorper arcu, eu volutpat lorem arcu sit amet lorem. Ut ac nulla et mauris tincidunt cursus vitae sit amet mi.</p>
    </article>

    <div class="rule"></div>

    <footer class="footer">
      <div class="footer__brand">
        <div class="footer__mark"></div>
        <div class="footer__name">Corwen Halstead</div>
      </div>
      <p class="footer__tagline">Capital Venture &amp; Investment Web Company</p>
      <p class="footer__contact">Lindenhofweg 12 40210 Altmark Germany<br>T: +31 600000123 | E: info@corwenhalstead.example</p>
      <p class="footer__prefs"><a href="#">Update your subscription preferences</a> to change which emails you receive from us<br><a href="#">Unsubscribe</a> from the Corwen Halstead newsletter</p>
      <div class="social">
        <a class="social__item" href="#" aria-label="Social profile"></a>
        <a class="social__item" href="#" aria-label="Social profile"></a>
      </div>
    </footer>
  </main>
</body>
</html>
```